Manuka Honey company needs a Upmarket, Luxury Website!

New Zealand, Taranaki based Manuka Honey company Marumaru Honey is looking for a new website, we are looking for an upmarket, luxury, serious website design. We export the highest quality quality Manuka Honey, straight from the Taranaki region.

Main export markets are Asia & Europe, also New Zealand & Australia.

Looking to have a beautiful, upmarket, serious, luxurious & graphical experience with mobile optimization in mind. Like the use of product staging/mockups

You can use copy from other websites to build the site and we will change the copy after the design is finished.

***Please include 'Honey Product' mockups in website.

*Will add illustrator files in coming days***

Feel free to make website functional in Shopify, Wordpress or WIX

Target Market(s)

Asia, Europe (main markets) New Zealand, Australia (Submarkets)

Coding

Coded - Design and coding required

Number of Pages Required

4 page

Requirements
Must have
• Home, Shop, About Us, Contact Us

Homepage to include:

Our Products
Company Video (video under construction)
What is MGO/UMF
Newsletter Opt-in

***(Not in Order)***

Please include 'Honey Product' mockups in website.
*Will add illustrator files in coming days
Nice to have
• FAQ & Partnership Inquiries (hyperlink in footer)

```html
<!DOCTYPE html>
<html lang="en">
<head>
<meta charset="utf-8">
<title>Marumaru Honey — The purest taste of New Zealand</title>
<link rel="stylesheet" href="https://fonts.googleapis.com/css2?family=DM+Serif+Display&family=Montserrat:wght@400;500;600&display=swap">
<style>
:root{
  --brown:#5c2b27;
  --footer:#6a3a35;
  --footer-dark:#5a2f2b;
  --text:#4a3a36;
  --gold:#e9c07a;
  --cream:#fdf3e7;
  --pattern:#f3dcc0;
  --line:#6b3a35;
  --white:#ffffff;
}
*{margin:0;padding:0;box-sizing:border-box}
html,body{width:1200px;height:4078px;overflow:hidden;background:var(--white)}
body{position:relative;font-family:"Montserrat",sans-serif;color:var(--text)}
.abs{position:absolute}
.serif{font-family:"DM Serif Display",serif;color:var(--brown);font-weight:400}
.btn{position:absolute;border:1.5px solid var(--line);color:var(--brown);font-size:13px;letter-spacing:.5px;display:flex;align-items:center;justify-content:center;text-transform:uppercase;background:transparent}
.fill{position:absolute}

/* header */
.brand{position:absolute;left:60px;top:24px;display:flex;align-items:center;gap:10px;font-size:15px;letter-spacing:2px;color:var(--brown);font-weight:500;text-transform:uppercase}
.brand .dot{width:26px;height:26px;border-radius:50%;background:var(--brown)}
.nav{position:absolute;top:29px;left:460px;display:flex;gap:40px;font-size:12px;font-weight:500;letter-spacing:.4px;color:var(--brown)}
.icons{position:absolute;top:25px;left:992px;display:flex;gap:24px}

/* hero */
.hero-title{left:58px;top:284px;line-height:1}
.hero-title .l1{font-size:52px;display:block}
.hero-title .l2{font-size:72px;display:block;margin-top:4px}
.hero-sub{left:58px;top:433px;font-size:16px;color:var(--text)}

/* story */
.body-text{font-size:13px;line-height:25px;text-align:justify;color:var(--text)}

/* products */
.section-title{position:absolute;left:0;width:1200px;text-align:center}
.rule{position:absolute;left:570px;width:60px;height:3px;background:var(--gold)}
.product{position:absolute;width:260px;text-align:center}
.product .jar{margin:0 auto;width:165px;height:190px;border-radius:16px 16px 22px 22px}
.product h3{font-family:"DM Serif Display",serif;font-weight:400;color:var(--brown);font-size:34px;margin-top:28px;line-height:1}
.product p{font-size:12px;line-height:17px;margin-top:14px;color:var(--text)}
.product .price{font-size:18px;margin-top:16px;color:#2b2220}
.product .stars{margin-top:12px}

/* umf */
.feature{position:absolute;left:177px;width:480px}
.feature .ic{position:absolute;left:0;top:0}
.feature h4{position:absolute;left:95px;top:-4px;font-family:"DM Serif Display",serif;font-weight:400;font-size:26px;color:var(--brown);white-space:nowrap}
.feature p{position:absolute;left:95px;top:34px;width:360px;font-size:12px;line-height:17px;color:#7a4a3a}

/* footer */
.footer{position:absolute;left:0;top:3858px;width:1200px;height:220px;background:var(--footer);color:#f3e6de}
.footer h5{position:absolute;font-size:11px;font-weight:600;letter-spacing:.6px;color:#fff}
.footer ul{position:absolute;list-style:none;font-size:12px;line-height:28px}
.copy{position:absolute;left:0;top:175px;width:1200px;height:45px;background:var(--footer-dark);font-size:11px;display:flex;align-items:center;justify-content:center;color:#f3e6de}
</style>
</head>
<body>

<!-- header -->
<div class="brand"><span class="dot"></span>Marumaru Honey</div>
<nav class="nav"><span>SHOP</span><span>OUR STORY</span><span>STOCKISTS</span><span>CONTACT US</span></nav>
<div class="icons">
  <svg width="18" height="18" viewBox="0 0 24 24" fill="none" stroke="#5c2b27" stroke-width="2"><path d="M12 21s-8-5-8-11a4.5 4.5 0 0 1 8-2.8A4.5 4.5 0 0 1 20 10c0 6-8 11-8 11z"/></svg>
  <svg width="18" height="18" viewBox="0 0 24 24" fill="none" stroke="#5c2b27" stroke-width="2"><circle cx="12" cy="8" r="4"/><path d="M4 21c1-5 15-5 16 0"/></svg>
  <svg width="22" height="22" viewBox="0 0 24 24" fill="none" stroke="#5c2b27" stroke-width="2"><path d="M5 8h12l-1 12H6z"/><path d="M8 8a3 3 0 0 1 6 0"/><circle cx="18" cy="18" r="4" fill="#d9412f" stroke="none"/></svg>
</div>

<!-- hero -->
<div class="fill" style="left:844px;top:66px;width:356px;height:600px;background:var(--pattern)" role="img" aria-label="Woven triangle pattern in soft sand tones"></div>
<div class="fill" style="left:586px;top:330px;width:190px;height:300px;border-radius:50%;background:radial-gradient(circle,#5fa834,#3f7f22 70%,transparent 72%)" role="img" aria-label="Fresh manuka leaves"></div>
<div class="fill" style="left:755px;top:264px;width:318px;height:356px;border-radius:26px 26px 40px 40px;background:linear-gradient(#1e1b1b 0 20%,#2a1812 20% 42%,#1d1a1a 42% 72%,#f6f1e6 72% 86%,#2a1812 86%)" role="img" aria-label="Jar of premium manuka honey with dark label"></div>
<h1 class="abs serif hero-title"><span class="l1">The purest taste of</span><span class="l2">New Zealand</span></h1>
<p class="abs hero-sub">A Manuka Honey You’ll love from a brand you can trust</p>
<div class="btn" style="left:58px;top:484px;width:175px;height:40px">Shop now</div>

<!-- our story -->
<div class="fill" style="left:0;top:792px;width:692px;height:503px;background:linear-gradient(120deg,#3a2a22,#7a5238 45%,#5a2a18 75%,#8a4a22)" role="img" aria-label="Honey dripping from a wooden dipper into a jar, company video"></div>
<svg class="abs" style="left:272px;top:1008px" width="86" height="86" viewBox="0 0 86 86"><circle cx="43" cy="43" r="40" fill="none" stroke="#fff" stroke-width="5"/><path d="M34 26l26 17-26 17z" fill="none" stroke="#fff" stroke-width="5" stroke-linejoin="round"/></svg>
<div class="fill" style="left:692px;top:863px;width:448px;height:432px;background:var(--cream)"></div>
<div class="fill" style="left:1105px;top:863px;width:35px;height:432px;background:var(--pattern)" role="img" aria-label="Narrow woven pattern border"></div>
<h2 class="abs serif" style="left:734px;top:900px;font-size:36px">Our Story</h2>
<p class="abs body-text" style="left:734px;top:964px;width:296px">Lorem ipsum dolor sit amet, consectetur adipiscing elit. Pellentesque nibh curabitur varius dui vitae, tincidunt aliquam morbi. Ut proin malesuada volutpat ullamcorper sollicitudin mauris consequat facilisi tristique. Faucibus mi vel ipsum aliquam. Vestibulum quam ante libero egestas curabitur faucibus proin at tempor.</p>
<div class="btn" style="left:734px;top:1206px;width:176px;height:40px">Learn more</div>

<!-- products -->
<h2 class="section-title serif" style="top:1394px;font-size:36px">Our products</h2>
<div class="rule" style="top:1452px"></div>
<p class="abs" style="left:380px;top:1482px;width:440px;text-align:center;font-size:13px;line-height:20px">Lorem ipsum dolor sit amet, consectetur adipiscing elit. Orci massa vitae risus lorem cursus sodales sed interdum. Aliquam varius non nunc id pellentesque faucibus.</p>

<div class="product" style="left:168px;top:1599px"><div class="jar" role="img" aria-label="Manuka honey jar, black label" style="background:linear-gradient(#1f1c1c 0 22%,#221a18 22% 80%,#2a1812 80%)"></div><h3>Honey</h3><p>Lorem ipsum dolor sit amet, consectetur adipiscing elit. Ultrices sem amet, lobortis eget cursus pharetra consequat libero ultrices. Aenean ipsum aliquet odio arcu sed ullamcorper.</p><div class="price">$45.90</div><svg class="stars" width="104" height="16" viewBox="0 0 104 16"><g fill="#f0c98a"><path id="st" d="M8 0l2.4 5 5.6.6-4.2 3.8 1.2 5.6L8 12.2 3 15l1.2-5.6L0 5.6 5.6 5z"/><use href="#st" x="22"/><use href="#st" x="44"/><use href="#st" x="66"/><use href="#st" x="88"/></g></svg></div>

<div class="product" style="left:478px;top:1599px"><div class="jar" role="img" aria-label="Manuka honey jar, black and cream label" style="background:linear-gradient(#1f1c1c 0 22%,#221a18 22% 62%,#f6f1e6 62% 82%,#2a1812 82%)"></div><h3>Honey</h3><p>Lorem ipsum dolor sit amet, consectetur adipiscing elit. Ultrices sem amet, lobortis eget cursus pharetra consequat libero ultrices. Aenean ipsum aliquet odio arcu sed ullamcorper.</p><div class="price">$45.90</div><svg class="stars" width="104" height="16" viewBox="0 0 104 16"><g fill="#f0c98a"><use href="#st"/><use href="#st" x="22"/><use href="#st" x="44"/><use href="#st" x="66"/><use href="#st" x="88"/></g></svg></div>

<div class="product" style="left:769px;top:1599px"><div class="jar" role="img" aria-label="Manuka honey jar, red and white label" style="background:linear-gradient(#1f1c1c 0 22%,#8a1c22 22% 30%,#f8f4ee 30% 80%,#2a1812 80%)"></div><h3>Honey</h3><p>Lorem ipsum dolor sit amet, consectetur adipiscing elit. Ultrices sem amet, lobortis eget cursus pharetra consequat libero ultrices. Aenean ipsum aliquet odio arcu sed ullamcorper.</p><div class="price">$45.90</div><svg class="stars" width="104" height="16" viewBox="0 0 104 16"><g fill="#f0c98a"><use href="#st"/><use href="#st" x="22"/><use href="#st" x="44"/><use href="#st" x="66"/><use href="#st" x="88"/></g></svg></div>

<div class="product" style="left:168px;top:2075px"><div class="jar" role="img" aria-label="Manuka honey jar, royal blue label" style="background:linear-gradient(#1f1c1c 0 22%,#1d3f8a 22% 82%,#2a1812 82%)"></div><h3>Honey</h3><p>Lorem ipsum dolor sit amet, consectetur adipiscing elit. Ultrices sem amet, lobortis eget cursus pharetra consequat libero ultrices. Aenean ipsum aliquet odio arcu sed ullamcorper.</p><div class="price">$45.90</div><svg class="stars" width="104" height="16" viewBox="0 0 104 16"><g fill="#f0c98a"><use href="#st"/><use href="#st" x="22"/><use href="#st" x="44"/><use href="#st" x="66"/><use href="#st" x="88"/></g></svg></div>

<div class="product" style="left:478px;top:2075px"><div class="jar" role="img" aria-label="Manuka honey jar, burnt orange label" style="background:linear-gradient(#1f1c1c 0 22%,#b0431e 22% 82%,#2a1812 82%)"></div><h3>Honey</h3><p>Lorem ipsum dolor sit amet, consectetur adipiscing elit. Ultrices sem amet, lobortis eget cursus pharetra consequat libero ultrices. Aenean ipsum aliquet odio arcu sed ullamcorper.</p><div class="price">$45.90</div><svg class="stars" width="104" height="16" viewBox="0 0 104 16"><g fill="#f0c98a"><use href="#st"/><use href="#st" x="22"/><use href="#st" x="44"/><use href="#st" x="66"/><use href="#st" x="88"/></g></svg></div>

<div class="product" style="left:769px;top:2075px"><div class="jar" role="img" aria-label="Manuka honey jar, purple label" style="background:linear-gradient(#1f1c1c 0 22%,#5b2a86 22% 82%,#2a1812 82%)"></div><h3>Honey</h3><p>Lorem ipsum dolor sit amet, consectetur adipiscing elit. Ultrices sem amet, lobortis eget cursus pharetra consequat libero ultrices. Aenean ipsum aliquet odio arcu sed ullamcorper.</p><div class="price">$45.90</div><svg class="stars" width="104" height="16" viewBox="0 0 104 16"><g fill="#f0c98a"><use href="#st"/><use href="#st" x="22"/><use href="#st" x="44"/><use href="#st" x="66"/><use href="#st" x="88"/></g></svg></div>

<div class="btn" style="left:513px;top:2545px;width:174px;height:42px">All products</div>

<!-- lorem section -->
<div class="fill" style="left:0;top:2686px;width:600px;height:493px;background:radial-gradient(circle at 45% 60%,#9a4e14,#c07a2e 35%,#e8dccb 62%,#f4efe6)" role="img" aria-label="Jar of honey with a wooden dipper, chamomile flowers and lemon"></div>
<div class="fill" style="left:600px;top:2686px;width:386px;height:493px;background:var(--cream)"></div>
<div class="fill" style="left:986px;top:2686px;width:214px;height:493px;background:var(--pattern)" role="img" aria-label="Woven triangle pattern in soft sand tones"></div>
<h2 class="abs serif" style="left:644px;top:2716px;font-size:36px">Lorem Ipsum</h2>
<p class="abs body-text" style="left:644px;top:2786px;width:298px;font-size:12px;line-height:24px">Lorem ipsum dolor sit amet, consectetur adipiscing elit. Pellentesque nibh curabitur varius dui vitae, tincidunt aliquam morbi. Ut proin malesuada volutpat ullamcorper sollicitudin mauris consequat facilisi tristique. Faucibus mi vel ipsum aliquam. Vestibulum quam ante libero egestas curabitur faucibus proin at tempor. Cras velit eget scelerisque volutpat id a vitae. Vel at tempus, amet iaculis enim blandit et. Cras velit eget scelerisque volutpat id a vitae. Vel at tempus, amet iaculis enim blandit et. Cras velit eget scelerisque volutpat id a vitae.</p>
<div class="btn" style="left:644px;top:3104px;width:176px;height:40px">Learn more</div>

<!-- umf -->
<h2 class="section-title serif" style="top:3300px;font-size:36px">What is UMF/MGO</h2>
<div class="rule" style="top:3368px"></div>

<div class="feature" style="top:3422px">
  <svg class="ic" width="60" height="76" viewBox="0 0 60 76" fill="none" stroke="#f0c98a" stroke-width="2"><path d="M10 2h32l12 12v50H10z"/><path d="M42 2v12h12M18 22h26M18 30h26M18 38h20"/><circle cx="16" cy="58" r="7"/><path d="M12 64l-2 10 6-3 6 3-2-10"/></svg>
  <h4>Certified</h4>
  <p>Convallis elementum ligula viverra turpis. Sollicitudin ultrices pretium et convallis sit auctor id. Mi lectus tincidunt orci sed facilisi aenean viverra.</p>
</div>
<div class="feature" style="top:3546px">
  <svg class="ic" width="64" height="64" viewBox="0 0 64 64" fill="none" stroke="#f0c98a" stroke-width="2"><path d="M14 4l10 6v12l-10 6-10-6V10z"/><path d="M24 22l10 6v12l-10 6-10-6V28z"/><path d="M4 28l10 6v12l-10 6"/><path d="M44 30c8 0 14 8 14 16s-6 14-14 14-14-6-14-14"/></svg>
  <h4>Premium Quality</h4>
  <p>Convallis elementum ligula viverra turpis. Sollicitudin ultrices pretium et convallis sit auctor id. Mi lectus tincidunt orci sed facilisi aenean viverra.</p>
</div>
<div class="feature" style="top:3668px">
  <svg class="ic" width="60" height="72" viewBox="0 0 60 72" fill="none" stroke="#f0c98a" stroke-width="2"><rect x="12" y="2" width="36" height="10" rx="2"/><rect x="6" y="12" width="48" height="58" rx="8"/><rect x="16" y="30" width="28" height="24" rx="3"/><circle cx="26" cy="44" r="4"/><circle cx="34" cy="44" r="4"/></svg>
  <h4>Certified</h4>
  <p>Convallis elementum ligula viverra turpis. Sollicitudin ultrices pretium et convallis sit auctor id. Mi lectus tincidunt orci sed facilisi aenean viverra.</p>
</div>

<div class="fill" style="left:738px;top:3420px;width:330px;height:330px;border-radius:50%;background:radial-gradient(circle,#e9c79a,#dcae76)" role="img" aria-label="Circular woven pattern in golden tones"></div>
<div class="fill" style="left:800px;top:3506px;width:206px;height:252px;border-radius:20px 20px 30px 30px;background:linear-gradient(#151313 0 24%,#1d1b1b 24%)" role="img" aria-label="Black jar of UMF 20+ manuka honey"></div>

<!-- footer -->
<footer class="footer">
  <div style="position:absolute;left:95px;top:28px;display:flex;align-items:center;gap:10px;font-size:15px;letter-spacing:2px;color:#fff;font-weight:500;text-transform:uppercase"><span style="width:24px;height:24px;border-radius:50%;background:#f3e6de"></span>Marumaru Honey</div>
  <p style="position:absolute;left:95px;top:74px;width:230px;font-size:11px;line-height:15px">Marumaru Honey is a part of a reforestation initiative and is very focused on providing a positive influence on the environment and community.</p>
  <h5 style="left:424px;top:30px">SITEMAP</h5>
  <ul style="left:424px;top:50px"><li>Shop</li><li>Our Story</li><li>Stockists</li><li>Contact Us</li></ul>
  <h5 style="left:598px;top:30px">HELP</h5>
  <ul style="left:598px;top:50px"><li>Stock Our Products</li><li>Refund Policy</li><li>Privacy Policy</li><li>Terms &amp; Conditions</li></ul>
  <h5 style="left:852px;top:30px">SIGN UP</h5>
  <div style="position:absolute;left:852px;top:53px;width:190px;height:32px;border:1px solid #d9c3b8;font-size:11px;padding:9px 10px;color:#e9d9cf">Enter email</div>
  <div style="position:absolute;left:1050px;top:53px;width:83px;height:32px;background:var(--gold);color:var(--brown);font-size:11px;font-weight:600;display:flex;align-items:center;justify-content:center">SEND</div>
  <svg style="position:absolute;left:852px;top:102px" width="110" height="30" viewBox="0 0 110 30" fill="none" stroke="#fff" stroke-width="1.5"><circle cx="14" cy="15" r="13"/><circle cx="54" cy="15" r="13"/><circle cx="94" cy="15" r="13"/></svg>
  <div class="copy">Copyright © 2021 All rights reserved.</div>
</footer>

</body>
</html>
```